International Trade Consulting Firm Seeks Quality Newsletter Design

Our company provides consulting services to Meridian 300 type companies. We compete with the largest consulting companies in the world. However, we have the highest level of expertise in the industry and need to look the most professional and high end. We have very relevant and important information to provide our customers about their compliance and projects. We will have the winning design coded to be an e-newsletter, so it needs to be one page. We want to keep our company colors and logo design in the newsletter, they are attached. We DO NOT want it to look like a mini-version of our website. We want a fresh look to this marketing piece. Newsletter will need to include title, possible sub-heading, space for a feature story, 2 other stories included, and space on either the left or right for short cuts, links or highlights of other articles. Contents/'In this issue' section, about us or branding area, section for relevant links, etc...
Target Market(s)
Meridian 300 companies, High-level management
Industry/Entity Type
Marketing

```html
<!DOCTYPE html>
<html lang="en">
<head>
<meta charset="utf-8">
<title>Foreign-Trade Zone News – Newsletter Layouts</title>
<link rel="stylesheet" href="https://fonts.googleapis.com/css2?family=Roboto+Condensed:wght@400;700&family=Arimo:wght@400;700&display=swap">
<style>
  :root{
    --stage:#8f8f8f;
    --ink-dark:#1f1f1f;
    --green-deep:#17451a;
    --green-head:#1a4d1c;
    --green-bright:#5aa83a;
    --green-mid:#3f7d2f;
    --khaki:#c8c27a;
    --khaki-line:#b9b06a;
    --lemon:#fff3a6;
    --star:#f3e27a;
    --paper:#ffffff;
    --body-text:#333333;
    --muted:#555555;

    --sheet-bg:var(--paper);
    --side-bg:var(--paper);
    --heading:var(--green-head);
    --text:var(--body-text);
    --logo-bg:#1e1e1e;
    --url-bg:#1e1e1e;
    --nav-title:var(--green-head);
    --nav-text:#333;
    --nav-feature:var(--lemon);
    --band-bg:var(--lemon);
    --band-text:var(--green-head);
    --divider:#e3e3e3;
  }
  *{box-sizing:border-box;margin:0;padding:0}
  html,body{width:1200px;height:900px;overflow:hidden}
  body{background:var(--stage);font-family:"Arimo",Arial,sans-serif;position:relative}

  .sheet{
    position:absolute;top:20px;width:522px;height:880px;
    background:var(--sheet-bg);
    box-shadow:0 0 6px rgba(0,0,0,.25);
    display:grid;grid-template-columns:174px 348px;
    grid-template-rows:118px 272px 318px 172px;
  }
  .sheet--light{left:63px}
  .sheet--dark{
    left:638px;
    --sheet-bg:#1e1e1e;--side-bg:#1e1e1e;
    --heading:var(--green-bright);--text:#e8e8e8;
    --logo-bg:#1f4a1f;--url-bg:#1f4a1f;
    --nav-title:var(--green-bright);--nav-text:#e0e0e0;
    --nav-feature:#1f5a1f;--band-bg:#1f4a1f;--band-text:var(--green-bright);
    --divider:#3a3a2a;
  }

  /* masthead */
  .brand{background:var(--logo-bg);display:flex;align-items:center;justify-content:center;padding:0 14px}
  .brand__name{font-family:"Roboto Condensed",Arial,sans-serif;font-weight:700;font-size:22px;line-height:1;color:var(--green-bright);text-transform:uppercase;text-align:center;letter-spacing:1px}
  .masthead{
    position:relative;padding:0 14px 0 16px;
    background:
      linear-gradient(115deg,rgba(255,255,255,0) 30%,rgba(120,190,90,.18) 38%,rgba(255,255,255,0) 46%,rgba(120,190,90,.15) 60%,rgba(255,255,255,0) 70%),
      linear-gradient(100deg,#0e3510,#2c6a28 45%,#114015 62%,#2a6126);
    border-bottom:1px solid #0b2a0c;
  }
  .masthead__date{position:absolute;top:18px;right:14px;font-family:"Roboto Condensed",Arial,sans-serif;font-weight:700;font-size:10px;color:#f3efc0}
  .masthead__title{position:absolute;top:36px;left:16px;font-family:"Roboto Condensed",Arial,sans-serif;font-weight:700;font-size:33px;line-height:1;color:#e6e6e6}
  .masthead__news{position:absolute;top:72px;left:16px;display:flex;align-items:baseline;gap:7px}
  .masthead__news-word{font-family:"Roboto Condensed",Arial,sans-serif;font-weight:700;font-size:37px;line-height:1;color:var(--khaki)}
  .masthead__tagline{font-family:"Roboto Condensed",Arial,sans-serif;font-weight:700;font-size:10px;color:#f4e96a}

  /* sidebar */
  .sidebar{background:var(--side-bg);border-right:1px solid var(--khaki-line)}
  .social{height:34px;background:#1e1e1e;display:flex;align-items:center;justify-content:space-around;padding:0 14px;border-bottom:1px solid #444}
  .social__dot{width:13px;height:13px;border-radius:50%;background:#f2f2f2}
  .site-url{height:30px;background:var(--url-bg);color:var(--green-bright);font-weight:700;font-size:10px;letter-spacing:1px;display:flex;align-items:center;justify-content:center;border-bottom:1px solid var(--khaki-line)}
  .issue-list{list-style:none;padding-top:10px}
  .issue-list__item{padding:4px 14px 5px 23px;height:48px}
  .issue-list__item--featured{background:var(--nav-feature)}
  .issue-list__title{font-family:"Roboto Condensed",Arial,sans-serif;font-weight:700;font-size:12.5px;color:var(--nav-title);text-transform:uppercase;line-height:1.2}
  .issue-list__text{font-size:7.2px;line-height:1.35;color:var(--nav-text)}

  .leader{padding:16px 14px 0 23px;border-top:1px solid var(--divider)}
  .leader__card{display:flex;align-items:center;gap:8px;margin-bottom:14px}
  .leader__photo{width:64px;height:64px;border-radius:50%;border:2px solid #fff;box-shadow:0 0 0 1px #333;background:radial-gradient(circle at 50% 40%,#c9a58a,#8c6a55 60%,#d9d9d9 62%)}
  .leader__name{font-family:"Roboto Condensed",Arial,sans-serif;font-weight:700;font-size:10px;color:var(--nav-title);text-transform:uppercase}
  .leader__role{font-size:8.5px;color:var(--green-mid)}
  .leader p{font-size:8.2px;line-height:1.68;color:var(--text);margin-bottom:11px}

  .about{padding:12px 14px 0 23px;border-top:1px solid var(--khaki-line)}
  .about__title{font-family:"Roboto Condensed",Arial,sans-serif;font-weight:700;font-size:12px;color:var(--nav-title)}
  .about__icon{display:block;margin:6px auto 8px 44px}
  .about__sub{font-weight:700;font-size:8.2px;color:var(--text);margin-bottom:3px}
  .about p{font-size:8.2px;line-height:1.68;color:var(--text)}

  /* main column */
  .story{padding:16px 16px 0 16px;position:relative}
  .story--lead{border-top:none}
  .story--second{border-top:1px solid var(--divider);padding-top:18px}
  .story__heading{font-family:"Roboto Condensed",Arial,sans-serif;font-weight:700;text-transform:uppercase;color:var(--heading);line-height:1.13}
  .story--lead .story__heading{font-size:35px;margin-bottom:9px}
  .story--second .story__heading{font-size:27px;margin-bottom:6px}
  .story__sub{display:flex;align-items:center;gap:6px;font-family:"Roboto Condensed",Arial,sans-serif;font-weight:700;font-size:11px;color:var(--heading);text-transform:uppercase;margin-bottom:6px}
  .story p{font-size:10.2px;line-height:1.75;color:var(--text)}
  .read-more{display:inline-flex;align-items:center;position:relative;margin-top:7px;height:22px;padding:0 14px 0 20px;border:1px solid var(--khaki-line);border-left:none;font-size:10.5px;color:var(--heading);text-transform:uppercase}
  .read-more svg{position:absolute;left:0;top:-1px}
  .story--second .read-more{position:absolute;left:16px;top:252px;margin:0}

  .feature{position:relative;border-top:1px solid var(--khaki-line)}
  .feature__star{position:absolute;left:-20px;top:-16px;z-index:2}
  .feature__photo{height:124px;background:linear-gradient(100deg,#e9e3d8,#c9b8a3 30%,#f1eee8 55%,#9aa3a9 78%,#d8cfc1)}
  .feature__label{position:absolute;left:12px;top:92px;background:#1e1e1e;color:#f0e7a8;font-size:10.5px;padding:4px 12px 4px 18px;text-transform:uppercase}
  .feature__band{background:var(--band-bg);height:48px;padding:6px 16px}
  .feature__heading{font-family:"Roboto Condensed",Arial,sans-serif;font-weight:700;font-size:33px;line-height:1.1;color:var(--band-text);text-transform:uppercase}
</style>
</head>
<body>

<!-- light edition -->
<article class="sheet sheet--light">
  <div class="brand"><span class="brand__name">Tradeway Consulting</span></div>
  <header class="masthead">
    <span class="masthead__date">16 APRIL 2014</span>
    <h1 class="masthead__title">Foreign-Trade Zone</h1>
    <div class="masthead__news"><span class="masthead__news-word">NEWS</span><span class="masthead__tagline">Important news about foreign-trade zones</span></div>
  </header>

  <aside class="sidebar">
    <div class="social"><span class="social__dot"></span><span class="social__dot"></span><span class="social__dot"></span><span class="social__dot"></span></div>
    <div class="site-url">www.tradewaygroup.com</div>
    <ul class="issue-list">
      <li class="issue-list__item"><div class="issue-list__title">Article 1</div><div class="issue-list__text">Editaquos rem restis dis imoditi ossitat aut aut pariberum fuga.</div></li>
      <li class="issue-list__item"><div class="issue-list__title">Article 2</div><div class="issue-list__text">Editaquos rem restis dis imoditi ossitat aut aut pariberum fuga.</div></li>
      <li class="issue-list__item issue-list__item--featured"><div class="issue-list__title">Featured Story</div><div class="issue-list__text">Editaquos rem restis dis imoditi ossitat aut aut pariberum fuga.</div></li>
      <li class="issue-list__item"><div class="issue-list__title">Article 3</div><div class="issue-list__text">Editaquos rem restis dis imoditi ossitat aut aut pariberum fuga.</div></li>
    </ul>
  </aside>
  <section class="story story--lead">
    <h2 class="story__heading">Heading title of<br>the article below</h2>
    <p>Lendae res nulpa cus, cum fugia volo quodipsus eiciis nullamus invera as et quiataq uoditin velent.</p>
    <p>Editaquos rem restis dis imoditi ossitat urestius aut aut pariberum faccus doloribus aut prem repedis et eosam fuga. It ipsum et quas dolorporiate natur se dolore eum ent modigen dandand anditate eicat apiet eicit omnis eum, arum evernat emquisti sus. Omnihilles derorro volo conse laut voloreh endite pre illa secabo.</p>
    <span class="read-more"><svg width="12" height="24" viewBox="0 0 12 24"><path d="M0 .5H2L11 12 2 23.5H0" fill="none" stroke="#b9b06a"/></svg>Read more</span>
  </section>

  <aside class="sidebar leader">
    <div class="leader__card">
      <div class="leader__photo" role="img" aria-label="Portrait of the chief executive"></div>
      <div><div class="leader__name">Dana Whitfield</div><div class="leader__role">CEO</div></div>
    </div>
    <p>Editaquos rem restis dis imoditi ossitat urestius aut aut pariberum faccus doloribus aut prem repedis et eosam fuga. Giam quis quiae vel incid etur?</p>
    <p>Erchiliquo culparciame nobitates ma por rem exerrun tibusti doluptiore dipsuntus Iciendant id quossedit, ius consequia debit alit expellore sin enet vendita sperfernamus autetur?</p>
  </aside>
  <section class="story story--second">
    <h2 class="story__heading">Smaller heading title<br>for longer title text</h2>
    <div class="story__sub"><svg width="24" height="8" viewBox="0 0 24 8"><path d="M0 4H22M18 1l4 3-4 3" fill="none" stroke="currentColor" stroke-width="1.5"/></svg>Here is possible subheading</div>
    <p>Lendae res nulpa cus, cum fugia volo quodipsus eiciis nullamus invera as et quiataq uoditin velent.</p>
    <p>Editaquos rem restis dis imoditi ossitat urestius aut aut pariberum faccus doloribus aut prem repedis et eosam fuga. It ipsum et quas dolorporiate natur se dolore eum ent modigen dandand anditate eicat apiet eicit omnis eum, arum evernat emquisti sus. Omnihilles derorro volo conse laut voloreh endite pre illa secabo.</p>
    <span class="read-more"><svg width="12" height="24" viewBox="0 0 12 24"><path d="M0 .5H2L11 12 2 23.5H0" fill="none" stroke="#b9b06a"/></svg>Read more</span>
  </section>

  <aside class="sidebar about">
    <h3 class="about__title">ABOUT US</h3>
    <svg class="about__icon" width="42" height="44" viewBox="0 0 42 44" fill="none" stroke="#b5a227" stroke-width="2"><path d="M14 2v7M20 2v7M26 2v7"/><path d="M4 16h28v14a8 8 0 0 1-8 8H12a8 8 0 0 1-8-8z"/><path d="M32 19h3a4 4 0 0 1 0 8h-3"/><path d="M2 42h32"/></svg>
    <div class="about__sub">OMNIHILLES DERORRO VLAUT</div>
    <p>Accabor eperum esciasi maionemquo excea volupta tibusam, et aut es ut impellu ptiusam est, officitate volorec</p>
  </aside>
  <section class="feature">
    <svg class="feature__star" width="32" height="32" viewBox="0 0 32 32"><path d="M16 1l4.4 9.6 10.6 1.2-7.9 7.2 2.2 10.4L16 24.2 6.7 29.4l2.2-10.4L1 11.8l10.6-1.2z" fill="#f3e27a"/></svg>
    <div class="feature__photo" role="img" aria-label="Photo of colleagues talking in a bright office"></div>
    <span class="feature__label">Featured story</span>
    <div class="feature__band"><h2 class="feature__heading">Heading title of</h2></div>
  </section>
</article>

<!-- dark edition -->
<article class="sheet sheet--dark">
  <div class="brand"><span class="brand__name">Tradeway Consulting</span></div>
  <header class="masthead">
    <span class="masthead__date">16 APRIL 2014</span>
    <h1 class="masthead__title">Foreign-Trade Zone</h1>
    <div class="masthead__news"><span class="masthead__news-word">NEWS</span><span class="masthead__tagline">Important news about foreign-trade zones</span></div>
  </header>

  <aside class="sidebar">
    <div class="social"><span class="social__dot"></span><span class="social__dot"></span><span class="social__dot"></span><span class="social__dot"></span></div>
    <div class="site-url">www.tradewaygroup.com</div>
    <ul class="issue-list">
      <li class="issue-list__item"><div class="issue-list__title">Article 1</div><div class="issue-list__text">Editaquos rem restis dis imoditi ossitat aut aut pariberum fuga.</div></li>
      <li class="issue-list__item"><div class="issue-list__title">Article 2</div><div class="issue-list__text">Editaquos rem restis dis imoditi ossitat aut aut pariberum fuga.</div></li>
      <li class="issue-list__item issue-list__item--featured"><div class="issue-list__title">Featured Story</div><div class="issue-list__text">Editaquos rem restis dis imoditi ossitat aut aut pariberum fuga.</div></li>
      <li class="issue-list__item"><div class="issue-list__title">Article 3</div><div class="issue-list__text">Editaquos rem restis dis imoditi ossitat aut aut pariberum fuga.</div></li>
    </ul>
  </aside>
  <section class="story story--lead">
    <h2 class="story__heading">Heading title of<br>the article below</h2>
    <p>Lendae res nulpa cus, cum fugia volo quodipsus eiciis nullamus invera as et quiataq uoditin velent.</p>
    <p>Editaquos rem restis dis imoditi ossitat urestius aut aut pariberum faccus doloribus aut prem repedis et eosam fuga. It ipsum et quas dolorporiate natur se dolore eum ent modigen dandand anditate eicat apiet eicit omnis eum, arum evernat emquisti sus. Omnihilles derorro volo conse laut voloreh endite pre illa secabo.</p>
    <span class="read-more"><svg width="12" height="24" viewBox="0 0 12 24"><path d="M0 .5H2L11 12 2 23.5H0" fill="none" stroke="#b9b06a"/></svg>Read more</span>
  </section>

  <aside class="sidebar leader">
    <div class="leader__card">
      <div class="leader__photo" role="img" aria-label="Portrait of the chief executive"></div>
      <div><div class="leader__name">Dana Whitfield</div><div class="leader__role">CEO</div></div>
    </div>
    <p>Editaquos rem restis dis imoditi ossitat urestius aut aut pariberum faccus doloribus aut prem repedis et eosam fuga. Giam quis quiae vel incid etur?</p>
    <p>Erchiliquo culparciame nobitates ma por rem exerrun tibusti doluptiore dipsuntus Iciendant id quossedit, ius consequia debit alit expellore sin enet vendita sperfernamus autetur?</p>
  </aside>
  <section class="story story--second">
    <h2 class="story__heading">Smaller heading title<br>for longer title text</h2>
    <div class="story__sub"><svg width="24" height="8" viewBox="0 0 24 8"><path d="M0 4H22M18 1l4 3-4 3" fill="none" stroke="#f3e27a" stroke-width="1.5"/></svg>Here is possible subheading</div>
    <p>Lendae res nulpa cus, cum fugia volo quodipsus eiciis nullamus invera as et quiataq uoditin velent.</p>
    <p>Editaquos rem restis dis imoditi ossitat urestius aut aut pariberum faccus doloribus aut prem repedis et eosam fuga. It ipsum et quas dolorporiate natur se dolore eum ent modigen dandand anditate eicat apiet eicit omnis eum, arum evernat emquisti sus. Omnihilles derorro volo conse laut voloreh endite pre illa secabo.</p>
    <span class="read-more"><svg width="12" height="24" viewBox="0 0 12 24"><path d="M0 .5H2L11 12 2 23.5H0" fill="none" stroke="#b9b06a"/></svg>Read more</span>
  </section>

  <aside class="sidebar about">
    <h3 class="about__title">ABOUT US</h3>
    <svg class="about__icon" width="42" height="44" viewBox="0 0 42 44" fill="none" stroke="#b5a227" stroke-width="2"><path d="M14 2v7M20 2v7M26 2v7"/><path d="M4 16h28v14a8 8 0 0 1-8 8H12a8 8 0 0 1-8-8z"/><path d="M32 19h3a4 4 0 0 1 0 8h-3"/><path d="M2 42h32"/></svg>
    <div class="about__sub">OMNIHILLES DERORRO VLAUT</div>
    <p>Accabor eperum esciasi maionemquo excea volupta tibusam, et aut es ut impellu ptiusam est, officitate volorec</p>
  </aside>
  <section class="feature">
    <svg class="feature__star" width="32" height="32" viewBox="0 0 32 32"><path d="M16 1l4.4 9.6 10.6 1.2-7.9 7.2 2.2 10.4L16 24.2 6.7 29.4l2.2-10.4L1 11.8l10.6-1.2z" fill="#f3e27a"/></svg>
    <div class="feature__photo" role="img" aria-label="Photo of colleagues talking in a bright office"></div>
    <span class="feature__label">Featured story</span>
    <div class="feature__band"><h2 class="feature__heading">Heading title of</h2></div>
  </section>
</article>

</body>
</html>
```